"Parcel Sheet Studio" Vendora Add-on Market Banner

Hey Designers! I need a photoshop banner to feature our web application, for use in the Vendora Add-on Market. See http://addons.vendora-example.com for examples of the other apps and their designs.
The image should be 310px wide x 100px tall. Suggested colors should be taken from our homepage: http://store.parcelsheetstudio-example.com/ and are also suggested below.
At minimum, the app banner must contain the name "Parcel Sheet Studio".
The application itself provides people with printable customized Invoice, Packing Slips templates, so imagery should reflect that in some way. Perhaps a printer or document icon for imagery.
I prefer flat design, or simple design without too much clutter or small details.
Target Market(s)
Adults based in United States, UK and Australia.. aged 25-35 who run online e-commerce businesses through Vendora.com
Industry/Entity Type
Printer
Requirements
Must have
- The words "Parcel Sheet Studio".
Black background, grey and white details.
Nice to have
- illustration style images, in flat design style if possible.
I like this type of design style: http://boxlayerweb-example.com/tour/overview/
Should not have
- Photo like images.
White background.

```html
<!DOCTYPE html>
<html lang="en">
<head>
<meta charset="utf-8">
<title>Parcel Sheet Studio – Add-on Market Banner</title>
<link rel="stylesheet" href="https://fonts.googleapis.com/css2?family=Montserrat:ital,wght@0,800;1,500&family=Open+Sans:wght@400;600&display=swap">
<style>
  :root {
    --canvas: #ffffff;
    --banner-bg: #000000;
    --banner-white: #ffffff;
    --banner-grey: #d4d4d4;
    --art-dark: #3a3a3a;
    --art-light: #9a9a9a;
    --card-border: #e3e3e3;
    --card-footer: #f7f7f7;
    --title-ink: #1f1f1f;
    --muted-ink: #6f6f6f;
    --tag-border: #dcdcdc;
    --star-on: #4a97d6;
    --star-off: #d8d8d8;
  }
  html, body {
    margin: 0;
    width: 1200px;
    height: 1200px;
    overflow: hidden;
    background: var(--canvas);
  }
  .canvas {
    position: relative;
    width: 1200px;
    height: 1200px;
  }
  .banner {
    position: absolute;
    left: 228px;
    width: 744px;
    height: 240px;
    background: var(--banner-bg);
    overflow: hidden;
  }
  .banner--standalone { top: 168px; }
  .banner--listing { top: 550px; }
  .banner__title {
    position: absolute;
    top: 12px;
    left: 0;
    right: 0;
    margin: 0;
    text-align: center;
    white-space: nowrap;
    font-family: "Montserrat", "Arial Black", sans-serif;
    font-weight: 800;
    font-size: 55px;
    letter-spacing: 4.5px;
    color: var(--banner-white);
  }
  .banner__art {
    position: absolute;
    left: 24px;
    top: 96px;
    width: 320px;
    height: 120px;
    background: linear-gradient(100deg, var(--art-light) 0%, var(--art-dark) 45%, var(--art-light) 100%);
    opacity: 0.55;
  }
  .banner__tagline {
    position: absolute;
    right: 29px;
    top: 80px;
    margin: 16px 0 0;
    text-align: right;
    font-family: "Montserrat", Arial, sans-serif;
  }
  .banner__feature {
    display: block;
    font-style: italic;
    font-weight: 500;
    font-size: 35px;
    line-height: 45px;
    color: var(--banner-grey);
  }
  .banner__claim {
    display: block;
    font-weight: 800;
    font-size: 34px;
    line-height: 50px;
    letter-spacing: 3px;
    color: var(--banner-white);
  }
  .listing {
    position: absolute;
    left: 228px;
    top: 790px;
    width: 742px;
    border: 1px solid var(--card-border);
    border-top: none;
    font-family: "Open Sans", Arial, sans-serif;
  }
  .listing__body {
    position: relative;
    height: 134px;
    padding: 0 34px;
  }
  .listing__name {
    position: absolute;
    top: 28px;
    left: 34px;
    margin: 0;
    font-weight: 600;
    font-size: 29px;
    color: var(--title-ink);
  }
  .listing__pricing {
    position: absolute;
    top: 68px;
    left: 34px;
    font-size: 28px;
    color: var(--muted-ink);
  }
  .listing__status {
    position: absolute;
    top: 29px;
    right: 40px;
    width: 127px;
    height: 44px;
    box-sizing: border-box;
    border: 2px solid var(--tag-border);
    text-align: center;
    line-height: 40px;
    font-size: 24px;
    color: var(--muted-ink);
  }
  .listing__footer {
    height: 72px;
    background: var(--card-footer);
    border-top: 1px solid var(--card-border);
    display: flex;
    align-items: center;
    justify-content: space-between;
    padding: 0 34px;
  }
  .rating { display: flex; gap: 3px; }
  .rating__star { width: 31px; height: 31px; }
  .rating__star--on { fill: var(--star-on); }
  .rating__star--off { fill: var(--star-off); }
  .listing__reviews {
    font-size: 30px;
    color: var(--muted-ink);
  }
</style>
</head>
<body>
<main class="canvas">

  <section class="banner banner--standalone">
    <h1 class="banner__title">Parcel Sheet Studio</h1>
    <div class="banner__art" role="img" aria-label="Flat grey printer illustration with printed sheets flying out to the right"></div>
    <p class="banner__tagline">
      <span class="banner__feature">Professional</span>
      <span class="banner__feature">Customizable</span>
      <span class="banner__claim">WITHOUT CODING</span>
    </p>
  </section>

  <section class="banner banner--listing">
    <h2 class="banner__title">Parcel Sheet Studio</h2>
    <div class="banner__art" role="img" aria-label="Flat grey printer illustration with printed sheets flying out to the right"></div>
    <p class="banner__tagline">
      <span class="banner__feature">Professional</span>
      <span class="banner__feature">Customizable</span>
      <span class="banner__claim">WITHOUT CODING</span>
    </p>
  </section>

  <article class="listing">
    <div class="listing__body">
      <h3 class="listing__name">Parcel Sheet Studio</h3>
      <span class="listing__pricing">Per Use</span>
      <span class="listing__status">Testing</span>
    </div>
    <div class="listing__footer">
      <div class="rating" aria-label="Rated 4 out of 5">
        <svg class="rating__star rating__star--on" viewBox="0 0 24 24"><polygon points="12,1.5 15.1,8.4 22.5,9.1 16.9,14 18.5,21.4 12,17.6 5.5,21.4 7.1,14 1.5,9.1 8.9,8.4"/></svg>
        <svg class="rating__star rating__star--on" viewBox="0 0 24 24"><polygon points="12,1.5 15.1,8.4 22.5,9.1 16.9,14 18.5,21.4 12,17.6 5.5,21.4 7.1,14 1.5,9.1 8.9,8.4"/></svg>
        <svg class="rating__star rating__star--on" viewBox="0 0 24 24"><polygon points="12,1.5 15.1,8.4 22.5,9.1 16.9,14 18.5,21.4 12,17.6 5.5,21.4 7.1,14 1.5,9.1 8.9,8.4"/></svg>
        <svg class="rating__star rating__star--on" viewBox="0 0 24 24"><polygon points="12,1.5 15.1,8.4 22.5,9.1 16.9,14 18.5,21.4 12,17.6 5.5,21.4 7.1,14 1.5,9.1 8.9,8.4"/></svg>
        <svg class="rating__star rating__star--off" viewBox="0 0 24 24"><polygon points="12,1.5 15.1,8.4 22.5,9.1 16.9,14 18.5,21.4 12,17.6 5.5,21.4 7.1,14 1.5,9.1 8.9,8.4"/></svg>
      </div>
      <span class="listing__reviews">3 reviews</span>
    </div>
  </article>

</main>
</body>
</html>
```